Dunmore Plumbing LLC business card

Would like a modern looking business card with my new logo

Contact Information for Business Card

Calvin Dunmore 2418 Elm Hollow Rd Larkfield, WX 06999, Dunmoreplumbingllc@exampletrade.com, 999-555-0174

```html
<!DOCTYPE html>
<html lang="en">
<head>
<meta charset="utf-8">
<title>Dunmore Plumbing LLC – Business Card</title>
<link href="https://fonts.googleapis.com/css2?family=Oswald:wght@400;500;600&family=Open+Sans:wght@400&display=swap" rel="stylesheet">
<style>
  :root {
    --blue: #00adef;
    --blue-light: #7fd3f7;
    --ink: #111111;
    --white: #ffffff;
    --backdrop: #eef1f4;
  }
  * { margin: 0; padding: 0; box-sizing: border-box; }
  html, body { width: 1200px; height: 548px; overflow: hidden; }
  body {
    background: var(--backdrop);
    display: flex;
    align-items: center;
    justify-content: center;
    gap: 40px;
    font-family: "Open Sans", sans-serif;
  }
  .card {
    position: relative;
    width: 540px;
    height: 312px;
    overflow: hidden;
    box-shadow: 0 2px 10px rgba(0,0,0,.12);
  }
  .card--front { background: var(--white); }
  .card--back { background: var(--blue); }

  .front-shape { position: absolute; inset: 0; width: 100%; height: 100%; }

  .brand {
    font-family: "Oswald", sans-serif;
    font-weight: 600;
    text-transform: uppercase;
    line-height: 1;
  }
  .brand__name { display: block; font-size: 38px; letter-spacing: 2px; text-align: center; }
  .brand__sub {
    display: flex;
    align-items: center;
    gap: 8px;
    font-size: 12px;
    letter-spacing: 3px;
    margin-top: 5px;
  }
  .brand__sub::before, .brand__sub::after {
    content: "";
    flex: 1;
    height: 1.5px;
    background: currentColor;
  }

  .card--front .brand { position: absolute; left: 42px; top: 40px; width: 224px; color: var(--ink); }

  .holder-name {
    position: absolute;
    left: 40px; top: 134px;
    font-family: "Oswald", sans-serif;
    font-weight: 500;
    font-size: 30px;
    letter-spacing: .5px;
    color: var(--blue);
    text-transform: uppercase;
    line-height: 1;
  }

  .contact {
    position: absolute;
    right: 46px; top: 164px;
    list-style: none;
    display: flex;
    flex-direction: column;
    align-items: flex-end;
    gap: 16px;
    color: var(--white);
    font-size: 12.5px;
    line-height: 1;
  }
  .contact__item { display: flex; align-items: center; gap: 9px; white-space: nowrap; }
  .contact__icon { width: 16px; height: 16px; flex: none; }

  .card--back .brand {
    position: absolute;
    left: 50%; top: 44px;
    width: 224px;
    transform: translateX(-50%);
    color: var(--white);
  }

  .services {
    position: absolute;
    left: 64px; right: 40px; top: 134px;
    display: grid;
    grid-template-columns: 1fr 1fr;
    column-gap: 30px;
    row-gap: 14px;
    list-style: none;
  }
  .services__item {
    display: flex;
    align-items: center;
    gap: 10px;
    font-family: "Oswald", sans-serif;
    font-weight: 400;
    font-size: 15.5px;
    letter-spacing: .3px;
    color: var(--white);
    text-transform: uppercase;
    line-height: 1.3;
  }
  .services__drop { width: 9px; height: 13px; flex: none; }
</style>
</head>
<body>

  <section class="card card--front" aria-label="Card front">
    <svg class="front-shape" viewBox="0 0 540 312" preserveAspectRatio="none" aria-hidden="true">
      <polygon points="0,312 0,300 528,0 540,0 540,312" fill="var(--blue-light)"/>
      <polygon points="12,312 540,10 540,312" fill="var(--blue)"/>
    </svg>

    <div class="brand">
      <span class="brand__name">Dunmore</span>
      <span class="brand__sub">Plumbing LLC</span>
    </div>

    <h1 class="holder-name">Calvin Dunmore</h1>

    <ul class="contact">
      <li class="contact__item">
        <svg class="contact__icon" viewBox="0 0 16 16" aria-hidden="true"><rect x="4" y="1" width="8" height="14" rx="1.5" fill="none" stroke="#fff" stroke-width="1.2"/><line x1="7" y1="13" x2="9" y2="13" stroke="#fff" stroke-width="1.2"/></svg>
        999-555-0174
      </li>
      <li class="contact__item">
        <svg class="contact__icon" viewBox="0 0 16 16" aria-hidden="true"><rect x="1" y="3.5" width="14" height="9" fill="none" stroke="#fff" stroke-width="1.1"/><polyline points="1,3.5 8,9 15,3.5" fill="none" stroke="#fff" stroke-width="1.1"/></svg>
        Dunmoreplumbingllc@exampletrade.com
      </li>
      <li class="contact__item">
        <svg class="contact__icon" viewBox="0 0 16 16" aria-hidden="true"><path d="M8 15s-5-5.2-5-8.6a5 5 0 0 1 10 0C13 9.8 8 15 8 15z" fill="none" stroke="#fff" stroke-width="1.1"/><circle cx="8" cy="6.4" r="1.8" fill="none" stroke="#fff" stroke-width="1.1"/></svg>
        2418 Elm Hollow Rd Larkfield, WX 06999
      </li>
    </ul>
  </section>

  <section class="card card--back" aria-label="Card back">
    <div class="brand">
      <span class="brand__name">Dunmore</span>
      <span class="brand__sub">Plumbing LLC</span>
    </div>

    <ul class="services">
      <li class="services__item"><svg class="services__drop" viewBox="0 0 9 13" aria-hidden="true"><path d="M4.5 0C4.5 0 0 6 0 8.5a4.5 4.5 0 0 0 9 0C9 6 4.5 0 4.5 0z" fill="var(--blue-light)"/></svg>Bathroom &amp; Kitchen</li>
      <li class="services__item"><svg class="services__drop" viewBox="0 0 9 13" aria-hidden="true"><path d="M4.5 0C4.5 0 0 6 0 8.5a4.5 4.5 0 0 0 9 0C9 6 4.5 0 4.5 0z" fill="var(--blue-light)"/></svg>Central Heating</li>
      <li class="services__item"><svg class="services__drop" viewBox="0 0 9 13" aria-hidden="true"><path d="M4.5 0C4.5 0 0 6 0 8.5a4.5 4.5 0 0 0 9 0C9 6 4.5 0 4.5 0z" fill="var(--blue-light)"/></svg>Boiler Change &amp; Repairs</li>
      <li class="services__item"><svg class="services__drop" viewBox="0 0 9 13" aria-hidden="true"><path d="M4.5 0C4.5 0 0 6 0 8.5a4.5 4.5 0 0 0 9 0C9 6 4.5 0 4.5 0z" fill="var(--blue-light)"/></svg>Friendly Service</li>
      <li class="services__item"><svg class="services__drop" viewBox="0 0 9 13" aria-hidden="true"><path d="M4.5 0C4.5 0 0 6 0 8.5a4.5 4.5 0 0 0 9 0C9 6 4.5 0 4.5 0z" fill="var(--blue-light)"/></svg>Underfloor Heating</li>
      <li class="services__item"><svg class="services__drop" viewBox="0 0 9 13" aria-hidden="true"><path d="M4.5 0C4.5 0 0 6 0 8.5a4.5 4.5 0 0 0 9 0C9 6 4.5 0 4.5 0z" fill="var(--blue-light)"/></svg>Free Evaluation</li>
      <li class="services__item"><svg class="services__drop" viewBox="0 0 9 13" aria-hidden="true"><path d="M4.5 0C4.5 0 0 6 0 8.5a4.5 4.5 0 0 0 9 0C9 6 4.5 0 4.5 0z" fill="var(--blue-light)"/></svg>System Upgrades</li>
      <li class="services__item"><svg class="services__drop" viewBox="0 0 9 13" aria-hidden="true"><path d="M4.5 0C4.5 0 0 6 0 8.5a4.5 4.5 0 0 0 9 0C9 6 4.5 0 4.5 0z" fill="var(--blue-light)"/></svg>Competitive Rates</li>
    </ul>
  </section>

</body>
</html>
```